Bright Meadow Party Coaches is excited to bring you Fenwick Valley’s Prime luxury limousine ser...

Leisure TransportationWedding DayWe will make your wedding day special and one to remember. Bright Meadow Party Coaches offers custom wedding transportation packages that are designed around your every need. Call our transportation consultant and learn how we can help you have a stress free and perfectly planned wedding event.PromsWe put safety first and give you piece of mind when we transport your loved ones.Special Occasions Bright Meadow Party Coaches professional chauffeured services will make any special event extraordinary. You will feel safe while our professional chauffeurs drive you in style and luxury.Corporate EventsNorth Coast Event Charters is a leader in professional chauffeured transportation services. Our highly trained staff will take the stress out of getting you to and from your destination. Bright Meadow Party Coaches is dedicated to the highest quality of services. Our top-of-the-line Calder-Voss Tramway is always safety inspected and cleaned before each use. Tours From the ocean to the redwoods, we offer tours to suit your needs.,Airport Service We are business ground travel experts. Our doo-to-door limousine can accommodate up to 10 passengers, and service all private and public airports

Target Market(s)

These brochures are going in motels and restaurants.

Font styles to use
Script

Colors
fed55c

Requirements
Must have
• Gold and black are the business colors. Check brand identity PDF

```html
<!DOCTYPE html>
<html lang="en">
<head>
<meta charset="utf-8">
<title>Bright Meadow Party Coaches – Trifold Brochure</title>
<link href="https://fonts.googleapis.com/css2?family=Cinzel:wght@400;700&family=Great+Vibes&family=Lato:ital,wght@0,400;0,700;1,400&display=swap" rel="stylesheet">
<style>
  :root {
    --backdrop: #8a8a8a;
    --ink: #0d0d0d;
    --panel: #141414;
    --gold: #d9ad4e;
    --gold-bright: #fed55c;
    --text: #d6d6d6;
    --muted: #a9a9a9;
    --photo-dark: #1f2326;
    --forest-a: #33452c;
    --forest-b: #14210f;
  }
  * { box-sizing: border-box; margin: 0; padding: 0; }
  html, body { width: 900px; height: 1200px; overflow: hidden; }
  body { background: var(--backdrop); font-family: "Lato", sans-serif; color: var(--text); position: relative; }

  .sheet { position: absolute; left: 40px; width: 820px; background: var(--ink); overflow: hidden; }
  .sheet--outside { top: 15px; height: 570px; }
  .sheet--inside { top: 605px; height: 580px; }
  .panel { position: absolute; top: 0; height: 100%; width: 273px; }
  .panel--1 { left: 0; } .panel--2 { left: 273px; } .panel--3 { left: 546px; width: 274px; }

  .photo { position: absolute; }
  .photo--chauffeur { left: 0; top: 0; width: 273px; height: 165px; background: linear-gradient(160deg, #2d3236, #0f1113); clip-path: polygon(0 0,100% 0,100% 80%,0 100%); }
  .photo--van-night { left: 0; top: 440px; width: 273px; height: 130px; background: linear-gradient(180deg, #3a3f44, #0b0c0d); clip-path: polygon(0 18%,100% 0,100% 100%,0 100%); }
  .photo--forest { left: 0; top: 0; width: 273px; height: 350px; background: linear-gradient(170deg, var(--forest-a), var(--forest-b)); clip-path: polygon(0 0,100% 0,100% 92%,0 100%); }
  .photo--van-forest { left: 0; top: 175px; width: 274px; height: 205px; background: linear-gradient(165deg, #4a5b3c, #1a2215 70%, #0c0c0c); clip-path: polygon(0 12%,100% 0,100% 88%,0 100%); }
  .photo--carpet { left: 18px; top: 180px; width: 237px; height: 118px; background: linear-gradient(135deg, #25282b, #5a1414 80%); }
  .photo--group { left: 0; top: 14px; width: 546px; height: 160px; background: linear-gradient(180deg, #6d7a80, #2a2c2e); }
  .photo--waterfront { left: 18px; top: 455px; width: 237px; height: 110px; background: linear-gradient(180deg, #7a8fa0, #2f3d3a 60%, #151515); }
  .photo--interior-a, .photo--interior-b { top: 312px; width: 112px; height: 78px; background: linear-gradient(135deg, #4b3a6a, #141018); }
  .photo--interior-a { left: 18px; } .photo--interior-b { left: 144px; background: linear-gradient(135deg, #2a3b66, #101218); }

  .gold-lines { position: absolute; left: 0; top: 0; width: 820px; height: 100%; pointer-events: none; }

  .heading { position: absolute; left: 18px; right: 18px; font-family: "Cinzel", serif; font-weight: 700; color: var(--gold); text-transform: uppercase; letter-spacing: 0.5px; }
  .heading--sm { font-size: 11px; }
  .heading--lg { font-size: 22px; }
  .copy { position: absolute; left: 18px; right: 18px; font-size: 7.6px; line-height: 1.42; color: var(--text); }
  .copy p + p { margin-top: 4px; }
  .copy--gold { color: var(--gold); font-size: 10px; line-height: 1.45; font-style: italic; }

  .book-button { position: absolute; left: 46px; top: 198px; width: 180px; padding: 5px 0; background: var(--gold-bright); color: var(--ink); font-family: "Cinzel", serif; font-weight: 700; font-size: 11px; text-align: center; }
  .call-line { position: absolute; left: 0; right: 0; top: 232px; text-align: center; font-family: "Cinzel", serif; font-size: 15px; color: #fff; }
  .call-line .phone { color: var(--gold-bright); }
  .online-line { position: absolute; left: 0; right: 0; top: 258px; text-align: center; font-size: 9px; color: #fff; }
  .online-line span { color: var(--gold-bright); }

  .contact-block { position: absolute; left: 0; right: 0; top: 410px; text-align: center; font-size: 8.5px; line-height: 1.9; color: var(--text); }
  .social { display: inline-flex; align-items: center; gap: 4px; }
  .social i { display: inline-block; width: 8px; height: 8px; background: var(--gold); }

  .brand { position: absolute; left: 0; right: 0; top: 70px; display: flex; align-items: center; justify-content: center; gap: 8px; font-family: "Cinzel", serif; font-size: 14px; color: var(--gold); }
  .brand i { width: 12px; height: 12px; border-radius: 50%; background: var(--gold); display: inline-block; }

  .title { position: absolute; left: 0; right: 0; top: 410px; text-align: center; font-family: "Cinzel", serif; font-weight: 700; font-size: 24px; line-height: 1.15; color: var(--gold); }
  .tagline { position: absolute; left: 0; right: 0; top: 472px; text-align: center; font-family: "Great Vibes", cursive; font-size: 20px; color: #fff; }
  .web-bar { position: absolute; left: 22px; right: 22px; top: 520px; padding: 4px 0; background: var(--gold-bright); color: var(--ink); text-align: center; font-family: "Cinzel", serif; font-size: 9px; font-weight: 700; }
</style>
</head>
<body>

<!-- Outside of the brochure -->
<section class="sheet sheet--outside">
  <div class="panel panel--1">
    <div class="photo photo--chauffeur" role="img" aria-label="Chauffeur in a tuxedo standing beside a black luxury coach"></div>
    <h2 class="heading heading--sm" style="top:180px">Mission Statement</h2>
    <div class="copy" style="top:200px">
      <p>Bright Meadow Party Coaches is excited to bring you Fenwick Valley’s Prime luxury limousine service. We believe every ride should feel as special as the event it carries you to, from the first greeting to the final farewell.</p>
      <p>Our mission is to offer safe, reliable and elegant travel for weddings, proms, tours, airport runs and corporate gatherings. Each trip is planned with care by a friendly team who know the valley roads and value your time.</p>
      <p>We keep our Calder-Voss Tramway spotless, inspected and ready, so you can relax, celebrate and enjoy the view while our chauffeurs handle every detail of the journey.</p>
    </div>
    <div class="photo photo--van-night" role="img" aria-label="Black luxury coach parked at night"></div>
  </div>

  <div class="panel panel--2">
    <div class="photo photo--forest" role="img" aria-label="Luxury coach on a road through a green forest"></div>
    <div class="book-button">Book Your Event Today!</div>
    <div class="call-line">Call us at <span class="phone">(555) 014-2290</span></div>
    <div class="online-line">Or book online at <span>www.brightmeadowcoaches.example</span></div>
    <div class="contact-block">
      www.brightmeadowcoaches.example<br>
      Serving all of Fenwick Valley<br>
      TCP permit #00000<br>
      <span class="social"><i></i><i></i> @brightmeadowcoaches</span>
    </div>
  </div>

  <div class="panel panel--3">
    <div class="brand"><i></i>Bright Meadow Party Coaches</div>
    <div class="photo photo--van-forest" role="img" aria-label="Black luxury coach parked on a forest drive"></div>
    <div class="title">Luxury<br>Transportation</div>
    <div class="tagline">for some of life’s biggest moments</div>
    <div class="web-bar">www.brightmeadowcoaches.example</div>
  </div>

  <svg class="gold-lines" viewBox="0 0 820 570" aria-hidden="true">
    <line x1="0" y1="165" x2="273" y2="132" stroke="#d9ad4e" stroke-width="2"/>
    <line x1="0" y1="463" x2="273" y2="440" stroke="#d9ad4e" stroke-width="2"/>
    <line x1="273" y1="350" x2="546" y2="322" stroke="#d9ad4e" stroke-width="2"/>
    <line x1="546" y1="200" x2="820" y2="175" stroke="#d9ad4e" stroke-width="2"/>
    <line x1="546" y1="380" x2="820" y2="356" stroke="#d9ad4e" stroke-width="2"/>
  </svg>
</section>

<!-- Inside of the brochure -->
<section class="sheet sheet--inside">
  <div class="panel panel--1">
    <h2 class="heading heading--lg" style="top:30px">About Us</h2>
    <div class="copy copy--gold" style="top:66px">Bright Meadow Party Coaches provides luxury transportation for some of life’s biggest moments. We offer more than just a ride; we invite you into a first-class experience for weddings, corporate events, tourists and more!</div>
    <div class="photo photo--carpet" role="img" aria-label="Guests stepping out of a coach onto a red carpet"></div>
    <h3 class="heading heading--sm" style="top:308px">The Red Carpet Experience</h3>
    <div class="copy" style="top:324px">Arrive like a star. Our chauffeurs roll out the red carpet, open your door and greet every guest by name, so the celebration begins the moment you step aboard.</div>
    <h3 class="heading heading--sm" style="top:390px">Onboard Luxury</h3>
    <div class="copy" style="top:406px">Relax in plush leather seating with soft mood lighting, a premium sound system, chilled refreshments and plenty of room for up to ten passengers. Every detail is designed for comfort, style and a smooth, quiet ride to your destination.</div>
  </div>

  <div class="panel panel--2">
    <div class="photo photo--group" role="img" aria-label="Group in formal wear standing outside a formalwear shop beside a coach"></div>
    <h3 class="heading heading--sm" style="top:196px">Personal, Customized Service</h3>
    <div class="copy" style="top:212px">
      <p>No two events are alike, and neither are our trips. Tell us your plans, timing and special wishes, and our consultant will craft a package that fits your day and your budget.</p>
      <p>From matching décor to favourite music, we shape each ride around you. Our team stays in touch before and during your event so every pickup is right on time.</p>
    </div>
    <h3 class="heading heading--sm" style="top:350px">Airport Service</h3>
    <div class="copy" style="top:366px">We are business ground travel experts. Our door-to-door limousine can accommodate up to 10 passengers, and serves all private and public airports. We track your flight and wait for you.</div>
    <div class="photo photo--waterfront" role="img" aria-label="Black coach parked by the water with hills behind"></div>
  </div>

  <div class="panel panel--3">
    <h3 class="heading heading--sm" style="top:186px">Wedding Day</h3>
    <div class="copy" style="top:202px">We will make your wedding day special and one to remember. Bright Meadow Party Coaches offers custom wedding transportation packages designed around your every need.</div>
    <h3 class="heading heading--sm" style="top:246px">Special Occasions</h3>
    <div class="copy" style="top:262px">Our professional chauffeured services will make any special event extraordinary. You will feel safe while we drive you in style.</div>
    <div class="photo photo--interior-a" role="img" aria-label="Coach interior with purple mood lighting"></div>
    <div class="photo photo--interior-b" role="img" aria-label="Coach interior with leather seating"></div>
    <h3 class="heading heading--sm" style="top:400px">Proms</h3>
    <div class="copy" style="top:416px">We put safety first and give you peace of mind when we transport your loved ones.</div>
    <h3 class="heading heading--sm" style="top:446px">Corporate Events</h3>
    <div class="copy" style="top:462px">Bright Meadow Party Coaches is a leader in chauffeured transportation. Our highly trained staff take the stress out of getting you to and from your destination.</div>
    <h3 class="heading heading--sm" style="top:516px">Tours</h3>
    <div class="copy" style="top:532px">From the ocean to the redwoods, we offer tours to suit your needs.</div>
  </div>

  <svg class="gold-lines" viewBox="0 0 820 580" aria-hidden="true">
    <line x1="18" y1="58" x2="120" y2="58" stroke="#d9ad4e" stroke-width="1.5"/>
    <line x1="273" y1="174" x2="820" y2="174" stroke="#d9ad4e" stroke-width="2"/>
  </svg>
</section>

</body>
</html>
```